Redesign of Smart Watch Gift Voucher-SEE ATTACHED CURRENT DESIGN

I need to redesign my existing design using all same content and elements.

MY ENVISION: I invision more of a professional advertisement type of flyer/voucher. Imagine how Quorrel.com would create a professionally looking flyer promoting the tavix or tavun.

you can get many ideas about professional design by looking at some of quorrels flyer designs :
https://www.findlery.example/search?q=tavix+advertisment&tbm=isch

stock photos are attached, you do not have to use them all, you can use some or none i am open to your designs using your own images if you want...just make sure the smartwatch looks black

DO NOT LEAVE ANY CONTENT OR ELEMENTS OUT ON MOCK UP PLEASE

SEE ATTACHED CURRENT DESIGN

I need to redesign my existing design using all same content and elements. DO NOT LEAVE ANY CONTENT OR ELEMENTS OUT ON MOCK UP PLEASE

Target Market(s)

B2B-you can get many ideas about professional design by looking at some of quorrels flyer designs :

Industry/Entity Type

Marketing

Requirements
Must have
• I need to redesign my existing design using all same content and elements. DO NOT LEAVE ANY CONTENT OR ELEMENTS OUT ON MOCK UP PLEASE

Nice to have

Should not have

```html
<!DOCTYPE html>
<html lang="en">
<head>
<meta charset="utf-8">
<title>Smart Watch Reward Voucher</title>
<link href="https://fonts.googleapis.com/css2?family=Roboto+Condensed:wght@300;400;700&family=Open+Sans:wght@600;700;800&display=swap" rel="stylesheet">
<style>
  :root {
    --ink: #1f1f1f;
    --heading-grey: #7a7a7a;
    --rule: #c9c9c9;
    --marker: #4a4a4a;
    --band-dark: #2d2d2d;
    --photo-light: #b9b4ae;
    --photo-mid: #8c8780;
    --photo-dark: #4f4c49;
    --panel-grey: #d6d6d6;
    --box-border: #7d7d7d;
    --muted: #8a8a8a;
    --white: #ffffff;
  }
  * { margin: 0; padding: 0; box-sizing: border-box; }
  html, body { width: 927px; height: 1200px; overflow: hidden; background: var(--white); }
  .voucher {
    position: relative; width: 927px; height: 1200px; overflow: hidden;
    background: var(--white); color: var(--ink);
    font-family: "Roboto Condensed", "Arial Narrow", sans-serif;
  }
  .voucher__backdrop { position: absolute; inset: 0; }
  .headline {
    position: absolute; right: 57px; text-align: right; color: var(--white);
    font-weight: 700; letter-spacing: -3px; line-height: 1;
  }
  .headline--small { font-size: 76px; top: 178px; line-height: 74px; }
  .headline--big { font-size: 116px; top: 336px; letter-spacing: -5px; }
  .tagline {
    position: absolute; right: 57px; top: 447px; font-size: 26px; font-weight: 300;
    color: var(--white); letter-spacing: -0.3px;
  }
  .intro {
    position: absolute; left: 48px; top: 445px; font-size: 12.6px; line-height: 16.4px;
    color: var(--ink); letter-spacing: -0.2px;
  }
  .rule { position: absolute; left: 0; width: 488px; height: 1px; background: var(--rule); }
  .section-marker { position: absolute; left: 0; width: 26px; height: 7px; background: var(--marker); }
  .section-title {
    position: absolute; left: 48px; font-size: 34px; font-weight: 700; color: var(--heading-grey);
    letter-spacing: -2px; line-height: 1;
  }
  .feature-list { position: absolute; list-style: none; font-size: 15.4px; line-height: 24.2px; color: var(--ink); }
  .feature-list li::before { content: "› "; }
  .section-copy {
    position: absolute; left: 48px; width: 450px; font-size: 13.6px; line-height: 18.3px;
    color: var(--ink); letter-spacing: -0.15px;
  }
  .redeem-box {
    position: absolute; left: 39px; top: 1018px; width: 849px; height: 144px;
    border: 1.5px solid var(--box-border); border-radius: 20px; background: var(--white);
    font-family: "Open Sans", Arial, sans-serif;
  }
  .redeem-box__meta { position: absolute; left: 0; top: 0; width: 240px; height: 100%; }
  .redeem-box__divider { position: absolute; left: 238px; top: 14px; width: 1px; height: 114px; background: var(--rule); }
  .meta-label { position: absolute; right: 10px; font-size: 17px; font-weight: 700; color: var(--ink); }
  .meta-value { position: absolute; right: 10px; font-size: 18px; font-weight: 700; color: var(--muted); letter-spacing: 0.5px; }
  .meta-rule { position: absolute; left: 52px; top: 73px; width: 178px; height: 1px; background: var(--rule); }
  .redeem-box__cta { position: absolute; left: 281px; top: 18px; }
  .cta-line { font-size: 19px; font-weight: 800; line-height: 30px; color: #333; letter-spacing: 0.1px; }
  .cta-url { font-size: 29px; font-weight: 800; color: var(--muted); letter-spacing: 0.6px; line-height: 36px; }
  .cta-terms { font-size: 13.5px; font-weight: 600; color: var(--ink); margin-top: 4px; }
</style>
</head>
<body>
<main class="voucher">
  <svg class="voucher__backdrop" width="927" height="1200" viewBox="0 0 927 1200">
    <defs>
      <linearGradient id="photoTone" x1="0" y1="0" x2="1" y2="1">
        <stop offset="0" stop-color="#cbbfb3"/>
        <stop offset="0.45" stop-color="#9a948d"/>
        <stop offset="1" stop-color="#5a5754"/>
      </linearGradient>
      <linearGradient id="panelTone" x1="0" y1="0" x2="1" y2="0">
        <stop offset="0" stop-color="#ffffff"/>
        <stop offset="0.35" stop-color="#e4e4e4"/>
        <stop offset="1" stop-color="#cfcfcf"/>
      </linearGradient>
      <radialGradient id="watchTone" cx="0.5" cy="0.45" r="0.6">
        <stop offset="0" stop-color="#3c3f44"/>
        <stop offset="1" stop-color="#15171a"/>
      </radialGradient>
    </defs>

    <rect x="0" y="0" width="927" height="560" fill="url(#photoTone)" role="img" aria-label="Photo of a wrist wearing a black smart fitness watch showing heart rate and activity data"/>
    <path class="top-band" d="M0 0 H927 V58 Q640 82 250 0 Z" fill="var(--band-dark)"/>

    <path class="wave-panel" d="M470 600 C640 560 800 540 927 528 V1000 C780 985 640 990 470 975 Z" fill="url(#panelTone)"/>
    <path class="wave-white" d="M0 392 C200 425 380 505 540 540 C680 560 820 548 927 540 V548 C800 566 640 580 470 600 C380 612 200 600 0 600 Z" fill="var(--white)"/>
    <path class="wave-grey" d="M520 548 C680 560 820 540 927 520 V545 C820 560 680 572 520 548 Z" fill="#9a9a9a"/>
    <rect x="0" y="560" width="470" height="440" fill="var(--white)"/>

    <rect x="548" y="582" width="340" height="360" rx="40" fill="url(#watchTone)" role="img" aria-label="Product shot of a black square smart watch with a rubber strap showing the time"/>
  </svg>

  <h1>
    <span class="headline headline--small">Enjoy Your<br>Brand New</span>
    <span class="headline headline--big">SMART WATCH</span>
  </h1>
  <p class="tagline">Take control of your life with your new smart fitness watch</p>

  <p class="intro">Congratulations, you<br>have been rewarded with a<br>Brand New Smart Fitness Watch<br>shipped right to your door. Just pay shipping<br>and handling. Your new Smart Fitness Watch has these<br>features: sport mode, pedometer, distance, calorie, heart rate, blood<br>pressure, stopwatch, sleep monitoring, phone locator, reminders, remote<br>camera, an alarm clock and much more!</p>

  <div class="rule" style="top:587px"></div>
  <div class="section-marker" style="top:612px"></div>
  <h2 class="section-title" style="top:600px">Features</h2>
  <ul class="feature-list" style="left:48px;top:630px"><li>Pedometer</li><li>Calorie Counter</li><li>Blood Pressure Monitor</li><li>Sleep Monitoring</li></ul>
  <ul class="feature-list" style="left:211px;top:630px"><li>Reminders Feature</li><li>Alarm Clock</li><li>Distance Tracker</li><li>Heart Rate Monitor</li></ul>
  <ul class="feature-list" style="left:344px;top:630px"><li>Stopwatch</li><li>Phone Locator</li><li>Remote Camera</li><li>Waterproof</li></ul>

  <div class="rule" style="top:738px"></div>
  <div class="section-marker" style="top:763px"></div>
  <h2 class="section-title" style="top:751px">How can we do this?</h2>
  <p class="section-copy" style="top:787px">We have a couple retail partners that we team up with to "crowd purchase" huge shipping containers that hold 10's of thousands of electronic products at 80-90% off retail. We simply pass our savings on to you as we do not profit from our electronic products. You are basically able to "piggy back" on our partnerships and buying power to get an attractive electronic premium for a fraction of the retail cost.</p>

  <div class="rule" style="top:892px"></div>
  <div class="section-marker" style="top:917px"></div>
  <h2 class="section-title" style="top:905px">What others say</h2>
  <p class="section-copy" style="top:941px">"Are you sure this is not a Korvana Stellar Smartwatch<br>in DISGUISE???? I love mine."<br>Wade T. Bayford City, NJ</p>

  <section class="redeem-box">
    <div class="redeem-box__meta">
      <span class="meta-label" style="top:12px">Certificate ID</span>
      <span class="meta-value" style="top:38px">91772-89218</span>
      <div class="meta-rule"></div>
      <span class="meta-label" style="top:82px">Expires</span>
      <span class="meta-value" style="top:108px">10/03/2020</span>
    </div>
    <div class="redeem-box__divider"></div>
    <div class="redeem-box__cta">
      <p class="cta-line">VIEW ALL THE DETAILS OF THIS SPECIAL OFFER</p>
      <p class="cta-line">AND REDEEM ONLINE AT</p>
      <p class="cta-url">WWW.PERKSANDBONUSHUB.COM</p>
      <p class="cta-terms">*Terms and Conditions apply see website for details</p>
    </div>
  </section>
</main>
</body>
</html>
```